Website design for Nutraceutical Contract Manufacturer in NJ

Develop website for a contract manufacturer, specializing in nutraceutical products. Our color theme is based on the colors of the American flag (Pantone blue no. 282 & red no. 193, white), representing a US presence of a company based in Italy. Our website will include a general e-mail box link for additional info. requests, color photos of our operation, a link to our parent company's website, a video, a mission statement, a description of our capabilities.Our internet presence will be on a B2B basis, to include a map of our location and contact information.

Target Market(s)

Businesses seeking contract manufacturer in the US nutraceutical industry.

Industry/Entity Type

Manufacturer

Number of Pages Required

3 page

Font styles to use
Sans Serif

Colors
3176b5
f04a50

Requirements
Must have
• Colors, as described in project description section. Three pages minimum - one to define what we do/location/contact info,/links to affiliated companies, one to showcase certifications, one to provide photos. We are open to having additional pages as suggested, if necessary. Our website for contacts info: www.veltracore-us.com .
• Link to our general email box: info@veltracore-us.com
• Pantone colors detailed in project description.
• HTTPS secure presence
Nice to have
• TBD
Should not have
• PROFANITY

```html
<!DOCTYPE html>
<html lang="en">
<head>
<meta charset="utf-8">
<title>Veltracore US — The Contract Manufacturer</title>
<link href="https://fonts.googleapis.com/css2?family=Montserrat:wght@400;500;600;700&family=Open+Sans:wght@400;600;700&display=swap" rel="stylesheet">
<style>
:root{
  --red:#c40f3e;
  --navy:#0b2a6b;
  --navy-card:#123a86;
  --pink-band:#fbeff3;
  --ink:#3b3b3b;
  --footer:#2a2a2a;
  --white:#ffffff;
}
*{box-sizing:border-box;margin:0;padding:0}
html,body{width:1200px;height:3147px;overflow:hidden}
body{position:relative;background:var(--white);font-family:"Open Sans",Arial,sans-serif;color:var(--ink)}
.abs{position:absolute}

/* header */
.site-header{position:absolute;left:0;top:0;width:1200px;height:109px;background:var(--white)}
.brand{position:absolute;left:99px;top:30px;font-family:"Montserrat",Arial,sans-serif;font-weight:600;font-size:36px;color:var(--navy);letter-spacing:.5px}
.main-nav{position:absolute;right:100px;top:44px;display:flex;gap:38px;font-family:"Montserrat",Arial,sans-serif;font-size:15.5px;font-weight:500;color:#222}
.main-nav .active{color:var(--red)}

/* hero */
.hero{position:absolute;left:0;top:109px;width:1200px;height:558px;overflow:hidden}
.hero-photo{position:absolute;inset:0;background:linear-gradient(180deg,#2f4c7a 0%,#5f7c8c 30%,#4d6a3a 60%,#3d5a26 100%)}
.hero-curve{position:absolute;left:0;top:0}
.hero-title{position:absolute;left:99px;top:76px;font-family:"Montserrat",Arial,sans-serif;font-weight:600;font-size:40px;color:var(--white);letter-spacing:1px}
.hero-sub{position:absolute;left:99px;top:133px;font-family:"Open Sans",Arial,sans-serif;font-weight:600;font-size:30px;color:var(--white)}
.hero-quote{position:absolute;left:99px;top:189px;width:620px;font-size:18px;line-height:28px;font-weight:600;color:var(--white)}
.btn-read{position:absolute;left:99px;top:281px;width:121px;height:53px;background:var(--red);border:2px solid #fff;color:#fff;font-family:"Montserrat",Arial,sans-serif;font-size:17px;display:flex;align-items:center;justify-content:center}
.hero-arrow{position:absolute;top:236px}

/* about */
.section-title{font-family:"Montserrat",Arial,sans-serif;font-weight:700;font-size:28px;color:var(--red)}
.section-sub{font-family:"Montserrat",Arial,sans-serif;font-weight:600;font-size:17.5px;color:var(--navy)}
.about-title{position:absolute;left:99px;top:748px}
.about-sub{position:absolute;left:99px;top:797px}
.about-text{position:absolute;left:99px;width:530px;font-size:14.2px;line-height:22px;color:#555}
.video{position:absolute;left:665px;top:753px;width:434px;height:283px;border:3px solid #ddd;box-shadow:0 18px 22px -12px rgba(0,0,0,.35);background:linear-gradient(120deg,#6d7d8d 0%,#c9d3dc 45%,#e9eef2 60%,#8393a0 100%)}
.video-bar{position:absolute;left:40px;right:40px;bottom:22px;height:5px;background:rgba(255,255,255,.5)}
.video-bar span{display:block;width:40%;height:100%;background:#3d8fd6}

/* capabilities */
.capabilities{position:absolute;left:0;top:1131px;width:1200px;height:537px;background:var(--pink-band)}
.center{text-align:center;width:1200px;left:0}
.cap-card{position:absolute;top:239px;width:245px;height:201px;color:#fff;text-align:center;box-shadow:0 14px 14px -10px rgba(0,0,0,.3)}
.cap-card.navy{background:linear-gradient(180deg,rgba(11,42,107,.95),rgba(18,58,134,.92))}
.cap-card.red{background:linear-gradient(180deg,rgba(196,15,62,.95),rgba(196,15,62,.9))}
.cap-icon{position:absolute;left:68px;top:-63px;width:108px;height:108px;border-radius:50%;border:4px solid #fff;display:flex;align-items:center;justify-content:center}
.cap-icon.red{background:var(--red)}
.cap-icon.navy{background:var(--navy)}
.cap-name{position:absolute;top:78px;width:100%;font-family:"Montserrat",Arial,sans-serif;font-weight:700;font-size:15.5px}
.cap-text{position:absolute;top:108px;left:20px;right:20px;font-size:12.5px;line-height:21px}
.cap-go{position:absolute;left:112px;top:172px}

/* mission */
.mission{position:absolute;left:0;top:1668px;width:1200px;height:405px;background:linear-gradient(180deg,#3d3d3d,#2c2c2c 55%,#3a3a3a)}
.mission-title{position:absolute;top:66px;font-family:"Montserrat",Arial,sans-serif;font-weight:700;font-size:28px;color:#fff}
.mission-rule{position:absolute;left:573px;top:118px;width:54px;height:2px;background:#fff}
.mission-text{position:absolute;left:100px;top:185px;width:1000px;text-align:center;font-weight:600;font-size:15.2px;line-height:37px;color:#fff}

/* testimonials */
.testi-title{position:absolute;top:2140px}
.testi-intro{position:absolute;left:170px;top:2200px;width:860px;text-align:center;font-size:14px;line-height:25px;color:#444}
.testi-card{position:absolute;top:2329px;width:445px;height:231px;padding:6px}
.testi-card.red{background:var(--red)}
.testi-card.navy{background:var(--navy)}
.testi-inner{width:100%;height:100%;border:2px dashed rgba(255,255,255,.85);display:flex;flex-direction:column;align-items:center;justify-content:center;text-align:center;color:#fff;padding:0 46px}
.testi-inner p{font-size:14px;line-height:26.5px;font-weight:600}
.testi-inner b{margin-top:12px;font-size:15px}
.quote-badge{position:absolute;width:76px;height:76px;border-radius:50%;border:4px solid #fff;display:flex;align-items:center;justify-content:center;font-family:Georgia,serif;font-weight:700;font-size:52px;color:#fff;line-height:1;padding-top:22px}

/* footer */
.site-footer{position:absolute;left:0;top:2677px;width:1200px;height:470px;background:var(--footer);color:#fff}
.footer-brand{position:absolute;top:92px;font-family:"Montserrat",Arial,sans-serif;font-weight:600;font-size:40px;color:#fff}
.social{position:absolute;left:482px;top:212px;display:flex;gap:7px}
.social span{width:43px;height:43px;border-radius:50%;border:2px solid #fff}
.footer-nav{position:absolute;top:312px;left:0;width:1200px;font-family:"Montserrat",Arial,sans-serif;font-weight:600;font-size:15px}
.footer-nav span{position:absolute;transform:translateX(-50%);white-space:nowrap}
.footer-rule{position:absolute;left:99px;top:382px;width:1002px;height:1px;background:#888}
.copyright{position:absolute;top:417px;font-size:13.5px;font-weight:600}
</style>
</head>
<body>

<header class="site-header">
  <div class="brand">Veltracore US</div>
  <nav class="main-nav">
    <span class="active">HOME</span><span>ABOUT US</span><span>AFFILIATES</span><span>CERTIFICATIONS</span><span>CONTACT US</span>
  </nav>
</header>

<section class="hero">
  <div class="hero-photo" role="img" aria-label="Photo of the manufacturing facility grounds with lawn, trees and a footpath"></div>
  <svg class="hero-curve" width="1200" height="558" viewBox="0 0 1200 558">
    <path d="M0 440 Q600 580 1200 440 L1200 558 L0 558 Z" fill="var(--red)"/>
    <path d="M0 457 Q600 660 1200 457 L1200 558 L0 558 Z" fill="#ffffff"/>
  </svg>
  <div class="hero-title">VELTRACORE</div>
  <div class="hero-sub">The Contract Manufacturer</div>
  <div class="hero-quote">"Veltracore US LLC is a contract manufacturer for the food supplements market, producing exclusively for third parties."</div>
  <div class="btn-read">Read More</div>
  <svg class="hero-arrow" style="left:34px" width="24" height="40" viewBox="0 0 24 40"><path d="M20 3 L4 20 L20 37" fill="none" stroke="#fff" stroke-width="2"/></svg>
  <svg class="hero-arrow" style="left:1142px" width="24" height="40" viewBox="0 0 24 40"><path d="M4 3 L20 20 L4 37" fill="none" stroke="#fff" stroke-width="2"/></svg>
</section>

<section class="about">
  <h2 class="section-title about-title">About Veltracore US</h2>
  <div class="section-sub about-sub">Specialising in nutraceutical products.</div>
  <p class="about-text" style="top:844px">Duis aute irure dolor in reprehenderit in voluptate velit esse cillum dolore eu fugiat nulla pariatur. Excepteur sint occaecat cupidatat non proident, sunt in culpa qui officia deserunt mollit anim id est laborum. Nemo enim ipsam voluptatem quia vo luptas sit aspernatur aut odit aut fugit, sed quia consequuntur magni dolores eos qui ratione voluptatem sequi nesciunt.</p>
  <p class="about-text" style="top:974px">Neque porro quisquam est, qui dolorem ipsum quia dolor sit amet, consectetur, adipisci velit, sed quia non numquam eius modi tempora incidunt ut labore et dolore magnam aliquam quaerat voluptatem.</p>
  <div class="video" role="img" aria-label="Company video still of a technician in a hairnet operating a production control panel">
    <svg class="abs" style="left:186px;top:110px" width="56" height="56" viewBox="0 0 56 56"><circle cx="28" cy="28" r="25" fill="rgba(0,0,0,.55)" stroke="#fff" stroke-width="3"/><path d="M22 17 L39 28 L22 39 Z" fill="#fff"/></svg>
    <div class="video-bar"><span></span></div>
  </div>
</section>

<section class="capabilities">
  <h2 class="section-title abs center" style="top:60px;text-align:center">Our Capabilities</h2>
  <div class="section-sub abs center" style="top:106px;text-align:center">Specialising in nutraceutical products.</div>

  <div class="cap-card navy" style="left:102px">
    <div class="cap-icon red"><svg width="50" height="50" viewBox="0 0 50 50" fill="none" stroke="#fff" stroke-width="2.4"><rect x="8" y="14" width="34" height="30"/><path d="M25 4v10M20 9h10"/><rect x="14" y="20" width="6" height="6"/><rect x="30" y="20" width="6" height="6"/><rect x="14" y="31" width="6" height="6"/><rect x="30" y="31" width="6" height="6"/><path d="M22 44v-9h6v9"/></svg></div>
    <div class="cap-name">VELTRACORE</div>
    <div class="cap-text">Nemo enim ipsam voluptatem quia voluptas sit aspernatur autodit</div>
    <svg class="cap-go" width="20" height="20" viewBox="0 0 20 20"><circle cx="10" cy="10" r="9" fill="#fff"/><path d="M6 10h8M10 6l4 4-4 4" stroke="var(--navy)" stroke-width="2.2" fill="none"/></svg>
  </div>
  <div class="cap-card red" style="left:352px">
    <div class="cap-icon navy"><svg width="54" height="50" viewBox="0 0 54 50" fill="none" stroke="#fff" stroke-width="2.4"><path d="M27 44 C10 32 5 24 5 16 A10 10 0 0 1 27 11 A10 10 0 0 1 49 16 C49 24 44 32 27 44 Z"/><path d="M8 25h12l4-7 5 13 4-6h13"/></svg></div>
    <div class="cap-name">NUTRACEUTICAL PRODUCTS</div>
    <div class="cap-text">Nemo enim ipsam voluptatem quia voluptas sit aspernatur autodit</div>
    <svg class="cap-go" width="20" height="20" viewBox="0 0 20 20"><circle cx="10" cy="10" r="9" fill="#fff"/><path d="M6 10h8M10 6l4 4-4 4" stroke="var(--red)" stroke-width="2.2" fill="none"/></svg>
  </div>
  <div class="cap-card navy" style="left:602px">
    <div class="cap-icon red"><svg width="50" height="50" viewBox="0 0 50 50" fill="none" stroke="#fff" stroke-width="2.4"><path d="M19 6h12M21 6v14L9 42h32L29 20V6"/><path d="M14 33h22"/><circle cx="22" cy="37" r="1.8" fill="#fff"/><circle cx="29" cy="36" r="1.4" fill="#fff"/></svg></div>
    <div class="cap-name">LAB FACILITIES</div>
    <div class="cap-text">Nemo enim ipsam voluptatem quia voluptas sit aspernatur autodit</div>
    <svg class="cap-go" width="20" height="20" viewBox="0 0 20 20"><circle cx="10" cy="10" r="9" fill="#fff"/><path d="M6 10h8M10 6l4 4-4 4" stroke="var(--navy)" stroke-width="2.2" fill="none"/></svg>
  </div>
  <div class="cap-card navy" style="left:852px">
    <div class="cap-icon red"><svg width="52" height="50" viewBox="0 0 52 50"><path d="M26 30 C15 22 13 17 13 13 A6 6 0 0 1 26 10 A6 6 0 0 1 39 13 C39 17 37 22 26 30 Z" fill="#fff"/><path d="M4 24 C6 34 12 40 20 44 M48 24 C46 34 40 40 32 44 M10 30 l8 8 M42 30 l-8 8" stroke="#fff" stroke-width="3" fill="none" stroke-linecap="round"/></svg></div>
    <div class="cap-name">OURS CAPABILITIES</div>
    <div class="cap-text">Nemo enim ipsam voluptatem quia voluptas sit aspernatur autodit</div>
    <svg class="cap-go" width="20" height="20" viewBox="0 0 20 20"><circle cx="10" cy="10" r="9" fill="#fff"/><path d="M6 10h8M10 6l4 4-4 4" stroke="var(--navy)" stroke-width="2.2" fill="none"/></svg>
  </div>
</section>

<section class="mission" role="img" aria-label="Darkened photo of the production floor with equipment">
  <h2 class="mission-title center" style="text-align:center">Our Mission</h2>
  <div class="mission-rule"></div>
  <p class="mission-text">The mission of Veltracore US is to be the premier contract manufacturer of dietary supplements in the United States, offering quality and excellence to our customers. Being a premier company does not mean being the biggest, but it does mean being the best in terms of customer service, employee talent and consistent growth. All Employees are committed to this vision and are always striving to exceed all standards of the industry.</p>
</section>

<section class="testimonials">
  <h2 class="section-title testi-title abs center" style="text-align:center">Our Testimonials</h2>
  <p class="testi-intro">Nemo enim ipsam voluptatem quia voluptas sit aspernatur aut odit aut fugit, sed quia consequuntur magni dolores eos qui ratione voluptatem sequi nesciunt.</p>

  <div class="testi-card red" style="left:107px">
    <div class="testi-inner">
      <p>Neque porro quisquam est, qui dolorem ipsum quia dolor sit amet, consectetur, adipisci velit, sed quia non numquam eius modi tempora incidunt ut labore et dolore magnam aliquam quaerat voluptatem. Ut enim ad minima veniam, quis nostrum...</p>
      <b>-Marla, NY</b>
    </div>
  </div>
  <div class="quote-badge" style="left:505px;top:2507px;background:var(--navy)">&ldquo;</div>

  <div class="testi-card navy" style="left:646px">
    <div class="testi-inner">
      <p>Neque porro quisquam est, qui dolorem ipsum quia dolor sit amet, consectetur, adipisci velit, sed quia non numquam eius modi tempora incidunt ut labore et dolore magnam aliquam quaerat voluptatem. Ut enim ad minima veniam, quis nostrum...</p>
      <b>-Peter, NY</b>
    </div>
  </div>
  <div class="quote-badge" style="left:625px;top:2299px;background:var(--red)">&ldquo;</div>
</section>

<footer class="site-footer">
  <div class="footer-brand center" style="text-align:center">Veltracore US</div>
  <div class="social" aria-label="Social media links">
    <span></span><span></span><span></span><span></span><span></span>
  </div>
  <nav class="footer-nav">
    <span style="left:197px">HOME</span><span style="left:275px">|</span>
    <span style="left:365px">ABOUT US</span><span style="left:459px">|</span>
    <span style="left:550px">AFFILIATES</span><span style="left:644px">|</span>
    <span style="left:759px">CERTIFICATIONS</span><span style="left:877px">|</span>
    <span style="left:976px">CONTACT US</span>
  </nav>
  <div class="footer-rule"></div>
  <div class="copyright center" style="text-align:center">Copyright © 2018 Veltracore. All Right Reserved</div>
</footer>

</body>
</html>
```